Over 100 ladies will be traveling to Ocean City, MD for a Women's Retreat Conference. This flyer is for advertisement. This flyer is to circulate for registrations as well as to post on social media. Theme is Holy Spirit fire. I have attached a photo. All the information in the attachment should be included on the flyer. Information should be clearly readable end eye catching.

Target Market(s)

Church ladies

Industry/Entity Type

Religious

Font styles to use
Sans Serif

Colors

Designer to choose colors to be used in the design.

Requirements
Must have
• Title: Brightvale Womens Gathering 2019 "FIRE"
• All components in attachments

```html
<!DOCTYPE html>
<html lang="en">
<head>
<meta charset="utf-8">
<title>Brightvale Womens Gathering 2019 "FIRE"</title>
<link href="https://fonts.googleapis.com/css2?family=Source+Sans+3:wght@400;600;700&display=swap" rel="stylesheet">
<style>
  :root {
    --ink: #0b0b0c;
    --maroon: #5a1f35;
    --plum: #3a1a34;
    --ember: #e8741c;
    --flame: #f6a531;
    --gold: #f2c25a;
    --gold-light: #fbe3a1;
    --gold-deep: #c8821f;
    --caption: #f3b64a;
    --band-text: #1b1208;
    --white: #ffffff;
    --muted: #e9e2da;
  }
  * { box-sizing: border-box; margin: 0; padding: 0; }
  html, body { width: 975px; height: 1200px; overflow: hidden; background: var(--ink); }
  body { font-family: "Source Sans 3", Arial, sans-serif; color: var(--white); }

  .flyer { position: relative; width: 975px; height: 1200px; background: var(--ink); }

  .top-rule {
    position: absolute; left: 0; top: 0; width: 100%; height: 18px;
    background: linear-gradient(90deg, var(--gold-deep), var(--gold-light) 50%, var(--gold-deep));
  }

  .hero {
    position: absolute; left: 0; top: 18px; width: 100%; height: 654px; overflow: hidden;
    background:
      radial-gradient(ellipse 190px 330px at 40px 360px, rgba(246,165,49,.95), rgba(232,116,28,.55) 45%, transparent 75%),
      radial-gradient(ellipse 190px 330px at 935px 360px, rgba(246,165,49,.95), rgba(232,116,28,.55) 45%, transparent 75%),
      radial-gradient(ellipse 520px 260px at 487px 120px, rgba(160,70,90,.55), transparent 75%),
      linear-gradient(180deg, var(--plum) 0%, var(--maroon) 45%, #2a0f1c 100%);
  }

  .title {
    position: absolute; left: 0; top: 50px; width: 100%; text-align: center;
    font-weight: 600; font-size: 33px; letter-spacing: .5px; color: var(--white);
  }
  .theme {
    position: absolute; left: 0; top: 84px; width: 100%; text-align: center;
    font-weight: 400; font-size: 118px; line-height: 1; letter-spacing: 4px;
    background: linear-gradient(180deg, var(--gold-light), var(--gold) 55%, var(--gold-deep));
    -webkit-background-clip: text; background-clip: text; color: transparent;
  }

  .portraits { position: absolute; left: 0; top: 0; width: 975px; height: 654px; }

  .caption {
    position: absolute; text-align: center; color: var(--caption);
    font-size: 14.5px; line-height: 1.3; font-weight: 400;
  }
  .caption strong { font-weight: 400; }
  .caption-left { left: 104px; top: 596px; width: 190px; }
  .caption-center { left: 392px; top: 630px; width: 190px; }
  .caption-right { left: 678px; top: 596px; width: 190px; }

  .venue {
    position: absolute; left: 0; top: 672px; width: 100%; height: 85px;
    background: linear-gradient(90deg, var(--gold-deep), var(--gold) 30%, var(--gold-light) 50%, var(--gold) 70%, var(--gold-deep));
    text-align: center; color: var(--band-text);
  }
  .venue-name { margin-top: 10px; font-weight: 700; font-size: 27px; letter-spacing: .3px; }
  .venue-address { font-weight: 400; font-size: 27px; line-height: 1.1; }

  .details { position: absolute; left: 0; top: 757px; width: 100%; height: 205px; background: var(--ink); }
  .included { position: absolute; left: 30px; top: 24px; width: 380px; }
  .included-heading { color: var(--caption); font-size: 17px; font-weight: 600; margin-bottom: 10px; }
  .included-list { list-style: none; }
  .included-list li {
    display: flex; align-items: center; gap: 10px;
    font-size: 16px; color: var(--white); height: 28.5px;
  }
  .included-list svg { flex: none; }
  .cost {
    display: inline-flex; align-items: baseline; gap: 12px; margin-top: 6px;
    border: 1.5px solid var(--gold); padding: 3px 12px; color: var(--caption);
  }
  .cost-price { font-weight: 700; font-size: 16px; }
  .cost-note { font-size: 12.5px; }

  .terms { position: absolute; left: 505px; top: 38px; width: 445px; font-size: 12.4px; line-height: 1.36; text-align: justify; }
  .terms p + p { margin-top: 14px; }
  .terms-policy { color: var(--muted); }
  .terms-contact { color: var(--caption); }

  .gallery { position: absolute; left: 0; top: 962px; width: 100%; height: 238px; display: flex; gap: 6px; }
  .gallery-tile { flex: 1; height: 100%; }
  .tile-beach { background: linear-gradient(180deg, #6d87a8 0%, #c9d3de 45%, #d8cdb3 68%, #2b4a63 100%); }
  .tile-lobby { background: linear-gradient(180deg, #6b5426 0%, #d2b46e 45%, #f1e3b8 70%, #4e6a3c 100%); }
  .tile-exterior { background: linear-gradient(180deg, #0d1a33 0%, #2b2f45 35%, #c99a63 70%, #5a3b24 100%); }
  .tile-suite { background: linear-gradient(180deg, #b7c3c9 0%, #e7ecee 40%, #ffffff 60%, #2f6b73 100%); }
</style>
</head>
<body>
<div class="flyer">
  <div class="top-rule"></div>

  <section class="hero" role="img" aria-label="Deep plum background with sparkling light and rising flames on both sides">
    <h1 class="title">BRIGHTVALE WOMENS GATHERING 2019</h1>
    <div class="theme">FIRE</div>

    <svg class="portraits" viewBox="0 0 975 654" aria-hidden="false">
      <defs>
        <linearGradient id="frameGold" x1="0" y1="0" x2="1" y2="1">
          <stop offset="0" stop-color="#fbe3a1"/>
          <stop offset=".5" stop-color="#f2c25a"/>
          <stop offset="1" stop-color="#c8821f"/>
        </linearGradient>
        <linearGradient id="portraitSide" x1="0" y1="0" x2="0" y2="1">
          <stop offset="0" stop-color="#e9e2d8"/>
          <stop offset=".55" stop-color="#b89c86"/>
          <stop offset="1" stop-color="#2a2326"/>
        </linearGradient>
        <linearGradient id="portraitCenter" x1="0" y1="0" x2="0" y2="1">
          <stop offset="0" stop-color="#efe6da"/>
          <stop offset=".5" stop-color="#c99a78"/>
          <stop offset="1" stop-color="#d9386a"/>
        </linearGradient>
      </defs>
      <g role="img" aria-label="Portrait of retreat speaker Pastor Renata Hollis">
        <polygon points="199,256 351,406 199,556 47,406" fill="url(#frameGold)"/>
        <polygon points="199,264 343,406 199,548 55,406" fill="url(#portraitSide)"/>
      </g>
      <g role="img" aria-label="Portrait of retreat speaker Pastor Corliss Ames">
        <polygon points="776,256 928,406 776,556 624,406" fill="url(#frameGold)"/>
        <polygon points="776,264 920,406 776,548 632,406" fill="url(#portraitSide)"/>
      </g>
      <g role="img" aria-label="Portrait of retreat host Apostle Delphine Marlowe">
        <polygon points="487,196 697,406 487,616 277,406" fill="url(#frameGold)"/>
        <polygon points="487,205 688,406 487,607 286,406" fill="url(#portraitCenter)"/>
      </g>
    </svg>

    <p class="caption caption-left">Retreat Speaker:<br>Pastor Renata Hollis<br>GCFM - Waldorf, Md.</p>
    <p class="caption caption-right">Retreat Speaker:<br>Pastor Corliss Ames<br>Orlando, Florida</p>
  </section>
  <p class="caption caption-center">Retreat Host:<br>Apostle Delphine Marlowe</p>

  <section class="venue">
    <h2 class="venue-name">SEABRIGHT MANOR HOTEL &amp; SUITES</h2>
    <p class="venue-address">4150 Seaboard Ave. Ocean City, Maryland 21842</p>
  </section>

  <section class="details">
    <div class="included">
      <h3 class="included-heading">INCLUDED:</h3>
      <ul class="included-list">
        <li><svg width="15" height="15" viewBox="0 0 16 16"><circle cx="8" cy="8" r="7" fill="none" stroke="#f2c25a" stroke-width="1.6"/><path d="M6.5 4.8 9.7 8 6.5 11.2" fill="none" stroke="#f2c25a" stroke-width="1.8"/></svg>All Retreat Sessions</li>
        <li><svg width="15" height="15" viewBox="0 0 16 16"><circle cx="8" cy="8" r="7" fill="none" stroke="#f2c25a" stroke-width="1.6"/><path d="M6.5 4.8 9.7 8 6.5 11.2" fill="none" stroke="#f2c25a" stroke-width="1.8"/></svg>2 Nights Hotel Accommodations</li>
        <li><svg width="15" height="15" viewBox="0 0 16 16"><circle cx="8" cy="8" r="7" fill="none" stroke="#f2c25a" stroke-width="1.6"/><path d="M6.5 4.8 9.7 8 6.5 11.2" fill="none" stroke="#f2c25a" stroke-width="1.8"/></svg>1 Hot Lunch Buffet</li>
        <li><svg width="15" height="15" viewBox="0 0 16 16"><circle cx="8" cy="8" r="7" fill="none" stroke="#f2c25a" stroke-width="1.6"/><path d="M6.5 4.8 9.7 8 6.5 11.2" fill="none" stroke="#f2c25a" stroke-width="1.8"/></svg>1 Full Hot American Breakfast</li>
      </ul>
      <div class="cost"><span class="cost-price">Cost: $295</span><span class="cost-note">*Based on double occupancy</span></div>
    </div>

    <div class="terms">
      <p class="terms-policy">**ALL deposits/registrations are NON-refundable and NON-transferable. Your entire registration is due by October 1, 2018. Please submit your desired roommate's name at the time of registration. If you do not choose a roommate one will be assigned to you unless you have registered for a private room.</p>
      <p class="terms-contact">Please contact Marisa via email marisa@delphinemarloweministries.org or phone 240-555-0148 for more information.</p>
    </div>
  </section>

  <section class="gallery">
    <div class="gallery-tile tile-beach" role="img" aria-label="Aerial view of the hotel on the beachfront"></div>
    <div class="gallery-tile tile-lobby" role="img" aria-label="Hotel lobby with staircase and warm lighting"></div>
    <div class="gallery-tile tile-exterior" role="img" aria-label="Hotel exterior lit up at night"></div>
    <div class="gallery-tile tile-suite" role="img" aria-label="Guest room with two beds"></div>
  </section>
</div>
</body>
</html>
```